Veltarum

Standard Business Card design.
Sample two-sided design uploaded. White front, Black back.
Would like white shield to be on all black background side.
Willing to look at a couple creative designs, but nothing crazy.
Preference for a classic, confident, strong design.

```html
<!DOCTYPE html>
<html lang="en">
<head>
<meta charset="UTF-8">
<title>Veltarum Business Card</title>
<link href="https://fonts.googleapis.com/css2?family=Montserrat:wght@400;500;700&display=swap" rel="stylesheet">
<style>
  :root {
    --backdrop: #3a3431;
    --card-white: #ffffff;
    --card-black: #1f1f1f;
    --ink: #1e1e1e;
    --ink-soft: #555555;
    --rule: #444444;
    --mark-block: #e6e6e6;
  }
  * { margin: 0; padding: 0; box-sizing: border-box; }
  html, body { width: 1200px; height: 786px; overflow: hidden; }
  body {
    background: var(--backdrop);
    font-family: "Montserrat", sans-serif;
    position: relative;
  }
  .card {
    position: absolute;
    top: 238px;
    width: 540px;
    height: 309px;
    overflow: hidden;
  }
  .card-front { left: 40px; background: var(--card-white); color: var(--ink); }
  .card-back { left: 620px; background: var(--card-black); color: var(--card-white); }

  .front-brand { position: absolute; left: 40px; top: 44px; }
  .brand-name {
    font-weight: 700;
    font-size: 34px;
    letter-spacing: 3px;
    line-height: 1;
  }
  .brand-rule { height: 1px; background: var(--rule); margin-top: 10px; width: 100%; }

  .front-edge-tab {
    position: absolute; left: 0; top: 178px;
    width: 8px; height: 30px; background: var(--ink);
  }
  .front-decor-block {
    position: absolute; right: -40px; top: -20px;
    width: 230px; height: 250px;
    background: var(--mark-block);
  }

  .contact { position: absolute; left: 40px; top: 140px; }
  .person-name { font-weight: 700; font-size: 17px; }
  .person-role { font-size: 10px; color: var(--ink-soft); margin-top: 1px; }
  .address { font-size: 11px; color: var(--ink-soft); margin-top: 12px; line-height: 1.35; }
  .contact-list { list-style: none; margin-top: 10px; font-size: 11px; color: var(--ink-soft); }
  .contact-list li { display: flex; align-items: center; gap: 8px; line-height: 1.6; }
  .contact-list svg { width: 10px; height: 10px; fill: var(--ink); }

  .back-brand {
    position: absolute; inset: 0;
    display: flex; flex-direction: column; align-items: center; justify-content: center;
  }
  .back-square { width: 46px; height: 46px; background: var(--card-white); margin-bottom: 18px; }
  .back-brand .brand-name { font-size: 40px; letter-spacing: 4px; }
  .back-brand .brand-rule { background: var(--card-white); width: 250px; margin-top: 12px; }
</style>
</head>
<body>
  <section class="card card-front">
    <div class="front-decor-block"></div>
    <div class="front-edge-tab"></div>
    <div class="front-brand">
      <div class="brand-name">VELTARUM</div>
      <div class="brand-rule"></div>
    </div>
    <div class="contact">
      <p class="person-name">Daniel Harrow</p>
      <p class="person-role">Owner</p>
      <p class="address">418 Linden Park Ave, #312<br>Brookfield, OH 44012</p>
      <ul class="contact-list">
        <li><svg viewBox="0 0 10 10"><path d="M2 0 L4 2.5 L3 3.5 Q4.5 6 6.5 7 L7.5 6 L10 8 L8.5 10 Q3 9 0 1.5 Z"/></svg>877-555-0148</li>
        <li><svg viewBox="0 0 10 10"><path d="M0 2 H10 V8 H0 Z M0 2 L5 6 L10 2" /></svg>info@veltarum.com</li>
        <li><svg viewBox="0 0 10 10"><circle cx="5" cy="5" r="5"/></svg>www.veltarum.com</li>
      </ul>
    </div>
  </section>

  <section class="card card-back">
    <div class="back-brand">
      <div class="back-square"></div>
      <div class="brand-name">VELTARUM</div>
      <div class="brand-rule"></div>
    </div>
  </section>
</body>
</html>
```